Yard sign design for high end luxury home builder.

Need a design for signage on custom homes that are being built. I already have a logo that I am satisfied with that needs to be incorporated. I need the following incorporated in the design of the sign-
- Lic number 318562
- phone number (555) 271-4038
- pendrickhomeworks.com
- Logo/Branding

If possible it may be nice to have the following quote that is on are business cards-

Quote from Osmund of Veltarra-
HE WHO WORKS WITH HIS HANDS IS A LABORER.
HE WHO WORKS WITH HIS HANDS & HIS HEAD IS A CRAFTSMAN.
HE WHO WORKS WITH HIS HANDS & HIS HEAD & HIS HEART IS AN ARTISAN.
-OSMUND OF VELTARRA

Target Market(s)

Archetect, Designers, Clients desiring to build a new home or remodel.

Colors
fde9d4
fee4d5
fabb94
fac994
faa54b
f68d4d
f37122
f78f20
f68e4e

Requirements
Must have
• - Lic number 318562
• - phone number (555) 271-4038
• - pendrickhomeworks.com
• - Logo/Branding
Nice to have
• Quote from Osmund of Veltarra-
• HE WHO WORKS WITH HIS HANDS IS A LABORER.
• HE WHO WORKS WITH HIS HANDS & HIS HEAD IS A CRAFTSMAN.
• HE WHO WORKS WITH HIS HANDS & HIS HEAD & HIS HEART IS AN ARTISAN.
• -OSMUND OF VELTARRA
• OR the below statement-
• Craftsmen that Care
Should not have
• Any additional verbiage not specified above including any type of verbiage about what kind of company we are. For instance- Integrity, reputable... It's just all played out. Im just looking for a bitching design that has the info that compliments my logo/branding.

```html
<!DOCTYPE html>
<html lang="en">
<head>
<meta charset="utf-8">
<title>Pendrick Homeworks – Yard Sign</title>
<link rel="stylesheet" href="https://fonts.googleapis.com/css2?family=Anton&family=Open+Sans:wght@600;800&display=swap">
<style>
  :root {
    --concrete-light: #d2d2d0;
    --concrete-mid: #a9a9a7;
    --concrete-dark: #8c8c8a;
    --panel-white: #ffffff;
    --mark-tan: #9c8466;
    --ink: #161616;
    --bar-dark: #1c1c1c;
    --band-orange: #f47f20;
    --footer-dark: #1e1e1e;
    --footer-mid: #3c3c3c;
    --text-white: #ffffff;
  }
  * { margin: 0; padding: 0; box-sizing: border-box; }
  html, body { width: 1200px; height: 800px; overflow: hidden; background: #ffffff; }

  .yard-sign { position: relative; width: 1200px; height: 800px; }

  .concrete-field {
    position: absolute; left: 0; top: 0; width: 1200px; height: 534px;
    background: radial-gradient(ellipse at 65% 30%, var(--concrete-light) 0%, var(--concrete-mid) 60%, var(--concrete-dark) 100%);
  }

  .brand-panel {
    position: absolute; left: 61px; top: 0; width: 451px; height: 534px;
    background: var(--panel-white);
  }
  .brand-square {
    position: absolute; left: 116px; top: 66px; width: 220px; height: 220px;
    background: var(--mark-tan);
  }
  .brand-name {
    position: absolute; left: 0; top: 338px; width: 451px; text-align: center;
    font-family: "Open Sans", sans-serif; font-weight: 800; font-size: 25px;
    color: var(--ink); line-height: 1.2; letter-spacing: 0.02em;
  }

  .license-bar {
    position: absolute; left: 0; top: 437px; width: 451px; height: 63px;
    background: var(--bar-dark); color: var(--text-white);
    font-family: "Open Sans", sans-serif; font-weight: 600; font-size: 38px;
    display: flex; align-items: center; justify-content: center;
  }

  .honoree-title {
    position: absolute; left: 540px; top: 146px; width: 640px; text-align: center;
    font-family: "Anton", sans-serif; font-weight: 400; font-size: 118px; line-height: 1.06;
    color: var(--ink);
    text-shadow: 3px 3px 0 #ffffff, -1px -1px 0 #ffffff, 1px -1px 0 #ffffff, -1px 1px 0 #ffffff, 6px 7px 6px rgba(0,0,0,0.35);
  }
  .honoree-title span { display: block; }

  .phone-band {
    position: absolute; left: 0; top: 534px; width: 1200px; height: 160px;
    background: var(--band-orange);
    display: flex; align-items: center; justify-content: center; gap: 36px;
  }
  .phone-icon { width: 112px; height: 112px; }
  .phone-number {
    font-family: "Open Sans", sans-serif; font-weight: 800; font-size: 100px;
    color: var(--text-white); letter-spacing: 0.01em; line-height: 1;
  }

  .web-band {
    position: absolute; left: 0; top: 694px; width: 1200px; height: 106px;
    background: linear-gradient(90deg, var(--footer-dark) 0%, var(--footer-mid) 100%);
    display: flex; align-items: center; justify-content: center;
  }
  .web-address {
    font-family: "Open Sans", sans-serif; font-weight: 600; font-size: 38px;
    color: var(--text-white); letter-spacing: 0.33em;
  }
</style>
</head>
<body>
<main class="yard-sign">
  <div class="concrete-field" role="img" aria-label="Grey textured concrete surface background"></div>

  <section class="brand-panel">
    <div class="brand-square"></div>
    <div class="brand-name">PENDRICK HOMEWORKS INC.</div>
    <div class="license-bar">Lic No 318562</div>
  </section>

  <h1 class="honoree-title"><span>OSMUND</span><span>OF VELTARRA</span></h1>

  <section class="phone-band">
    <svg class="phone-icon" viewBox="0 0 112 112" aria-hidden="true">
      <circle cx="56" cy="56" r="50" fill="none" stroke="#ffffff" stroke-width="7"/>
      <path d="M38 30 l10 -4 l8 16 l-7 5 c3 8 8 14 15 18 l6 -6 l15 9 l-4 10 c-3 4 -9 5 -14 3 c-15 -6 -28 -20 -33 -36 c-2 -6 0 -12 4 -15 z" fill="#ffffff"/>
    </svg>
    <div class="phone-number">(555) 271-4038</div>
  </section>

  <footer class="web-band">
    <div class="web-address">www.PendrickHomeworks.com</div>
  </footer>
</main>
</body>
</html>
```